Maplecrest Learning Center Posters Showing Building Blocks

We need poster designs for a School in Arizona for kids with Autism. There will be 4 such posters needed which highlight our schools building blocks. Requirements for all 4 posters are as followed: 1) We need the Maplecrest Learning Center Logo on each poster. I have included attachment. 2) The posters need the following titles: Building Block #1 (for the first poster), Building Block #2 for the 2nd poster, Building Block #3 for the 3rd poster, and Building Block #4 for the forth poster. 3) The main text and focus of the posters will be the following key words: For the first poster the words "Kids first in every decision". The words for the second poster are: "Students are friends with each other, and welcome new students with open arms." The words for the 3rd poster are: "The school is quiet, and students are working hard to do their best." The words for the 4th poster are: "Parents see amazing improvement in their child." 4) We would love to use some of the kids art from our schools if possible. Use your expertise to decide. I will send these out as well. 5) Try and design the posters around the key words from each poster 6) I am sure if landscape or portrait would be best so I will let the experts decide. All 4 posters need to be the same layout once decided.

Target Market(s)

These posters are for the school only. Prospective students/parents will see these posters so they will be used for Marketing from that perspective. We may put out into local community in future.

Industry/Entity Type

School

Font styles to use
Serif

Requirements
Must have
• 1) Logo (Maplecrest Learning Center for Growth and Discovery)
• 2) Title: as described in write up
• 3) Key words: as described in write up
Nice to have
• Kids art from school. Note: This is the first time that I have been on this site so I may have made a mistake by putting 4 posters on one project. I am assuming that I would need to pay more to have 4 posters so let me know if I need to modify the project in any way?

```html
<!DOCTYPE html>
<html lang="en">
<head>
<meta charset="utf-8">
<title>Maplecrest Learning Center – Building Block Posters</title>
<link rel="stylesheet" href="https://fonts.googleapis.com/css2?family=Abril+Fatface&family=Courier+Prime:ital,wght@0,400;0,700;1,700&display=swap">
<style>
  :root {
    --page: #ffffff;
    --paper: #f5f5f3;
    --ink: #111111;
    --brand-ink: #1c2a5a;
    --brand-rule: #c8323c;
    --block1-a: #5fb8e6;
    --block1-b: #e9f5fc;
    --block2-a: #e0468f;
    --block2-b: #fbe3ef;
    --block3-a: #f6c86a;
    --block3-b: #f4a7a0;
    --block3-c: #fdf0c8;
    --block4-a: #6fb8e0;
    --block4-b: #e3ea7a;
    --block4-c: #58b98a;
  }
  * { box-sizing: border-box; margin: 0; padding: 0; }
  html, body {
    width: 873px;
    height: 1200px;
    overflow: hidden;
    background: var(--page);
  }
  .poster-set {
    position: relative;
    width: 873px;
    height: 1200px;
  }
  .poster {
    position: absolute;
    width: 360px;
    height: 480px;
    background: var(--paper);
    overflow: hidden;
  }
  .poster--1 { left: 47px;  top: 47px; }
  .poster--2 { left: 478px; top: 47px; }
  .poster--3 { left: 47px;  top: 601px; }
  .poster--4 { left: 478px; top: 601px; }

  .poster__art {
    position: absolute;
    left: 0; top: 0;
    width: 360px;
    height: 428px;
  }
  .poster--1 .poster__art {
    background:
      radial-gradient(circle at 30% 35%, var(--block1-b) 0 18%, transparent 40%),
      radial-gradient(circle at 75% 70%, var(--block1-b) 0 14%, transparent 38%),
      linear-gradient(160deg, var(--block1-a), #9ad3f0 55%, var(--block1-b));
  }
  .poster--2 .poster__art {
    background:
      radial-gradient(ellipse at 55% 50%, #f3a0c6 0 20%, transparent 55%),
      linear-gradient(170deg, var(--block2-a), #ee86b7 50%, var(--block2-b) 95%);
  }
  .poster--3 .poster__art {
    background:
      radial-gradient(ellipse at 45% 20%, var(--block3-b) 0 15%, transparent 45%),
      linear-gradient(170deg, var(--block3-c), var(--block3-a) 45%, #f7d98c 70%, var(--block3-b));
  }
  .poster--4 .poster__art {
    background:
      radial-gradient(circle at 25% 45%, var(--block4-b) 0 12%, transparent 30%),
      radial-gradient(circle at 55% 35%, var(--block4-b) 0 12%, transparent 30%),
      linear-gradient(180deg, var(--block4-a), #a8d6e6 40%, #cfe6a8 70%, var(--block4-c));
  }

  .poster__title {
    position: absolute;
    left: 64px;
    top: 160px;
    font-family: "Abril Fatface", serif;
    font-weight: 400;
    font-size: 60px;
    line-height: 66px;
    color: var(--ink);
    letter-spacing: 0.5px;
  }
  .poster__words {
    position: absolute;
    font-family: "Courier Prime", monospace;
    font-weight: 700;
    font-style: italic;
    font-size: 12.5px;
    line-height: 25px;
    color: var(--ink);
  }
  .poster--1 .poster__words { right: 28px; top: 298px; text-align: right; }
  .poster--2 .poster__words { right: 24px; top: 298px; text-align: right; }
  .poster--3 .poster__words { right: 26px; top: 298px; text-align: right; }
  .poster--4 .poster__words { left: 106px; top: 296px; width: 230px; text-align: left; }

  .brand {
    position: absolute;
    left: 8px;
    top: 444px;
    display: flex;
    align-items: center;
    gap: 6px;
  }
  .brand__square {
    width: 16px;
    height: 16px;
    background: var(--brand-ink);
  }
  .brand__name {
    font-family: "Courier Prime", monospace;
    font-weight: 400;
    font-size: 7px;
    line-height: 9px;
    color: var(--brand-ink);
  }
</style>
</head>
<body>
<main class="poster-set">

  <article class="poster poster--1">
    <div class="poster__art" role="img" aria-label="Child's blue crayon drawing of overlapping circles"></div>
    <h2 class="poster__title">Building<br>Block #1</h2>
    <p class="poster__words">Kids first in every decision</p>
    <div class="brand">
      <span class="brand__square"></span>
      <span class="brand__name">MAPLECREST LEARNING CENTER<br>for Growth and Discovery</span>
    </div>
  </article>

  <article class="poster poster--2">
    <div class="poster__art" role="img" aria-label="Child's pink watercolour painting of a patterned heart"></div>
    <h2 class="poster__title">Building<br>Block #2</h2>
    <p class="poster__words">Students are friends with each other, and<br>welcome new students with open arms</p>
    <div class="brand">
      <span class="brand__square"></span>
      <span class="brand__name">MAPLECREST LEARNING CENTER<br>for Growth and Discovery</span>
    </div>
  </article>

  <article class="poster poster--3">
    <div class="poster__art" role="img" aria-label="Child's warm watercolour painting of a town with a winding road, clouds and a plane"></div>
    <h2 class="poster__title">Building<br>Block #3</h2>
    <p class="poster__words">The school is quiet, and students are<br>working hard to do their best</p>
    <div class="brand">
      <span class="brand__square"></span>
      <span class="brand__name">MAPLECREST LEARNING CENTER<br>for Growth and Discovery</span>
    </div>
  </article>

  <article class="poster poster--4">
    <div class="poster__art" role="img" aria-label="Child's painting of bright round flowers on tall stems under a blue sky"></div>
    <h2 class="poster__title">Building<br>Block #4</h2>
    <p class="poster__words">Parents see amazing improvement in<br>their child</p>
    <div class="brand">
      <span class="brand__square"></span>
      <span class="brand__name">MAPLECREST LEARNING CENTER<br>for Growth and Discovery</span>
    </div>
  </article>

</main>
</body>
</html>
```